Lumen Consulting

We need a web design for a new supply chain consulting business. we will work with major brands in the electronics, apparel, toy and jewelry industries to create a sustainability program for our customers and implement in their supply chain. We want our customers to have confidence in their supply chain responsibility program. We also manage stakeholder engagements, NGO relationships, and external communications.

I would like to colors to be green, orange and/or black to match the logo (attached). The final design should communicate positive and optimistic leadership - for a professional, sustainable, business.

Industry/Entity Type

Business

```html
<!DOCTYPE html>
<html lang="en">
<head>
<meta charset="utf-8">
<title>Lumen Consulting</title>
<link href="https://fonts.googleapis.com/css2?family=Bebas+Neue&family=Open+Sans:ital,wght@0,300;0,400;0,600;1,400&display=swap" rel="stylesheet">
<style>
:root{
  --green:#8dc63f;
  --green-light:#a8e05a;
  --orange:#f29c1f;
  --orange-dark:#e8901a;
  --ink:#1e1e1e;
  --text:#555555;
  --white:#ffffff;
  --footer:#1f1f1f;
}
*{margin:0;padding:0;box-sizing:border-box}
html,body{width:938px;height:1200px;overflow:hidden;background:var(--white)}
body{position:relative;font-family:"Open Sans",sans-serif;color:var(--ink)}
.top-bar{position:absolute;left:0;top:0;width:938px;height:6px;background:var(--green)}
.site-header{position:absolute;left:0;top:6px;width:938px;height:174px}
.brand{position:absolute;left:319px;top:92px;width:300px;text-align:center}
.brand-name{font-family:"Open Sans",sans-serif;font-weight:400;font-size:28px;color:var(--ink);line-height:1;white-space:nowrap}
.main-nav a{position:absolute;top:132px;font-size:11px;color:var(--ink);text-decoration:none;text-transform:uppercase}
.main-nav a.is-active{color:var(--orange)}
.nav-marker{position:absolute;left:40px;top:168px;width:37px;height:6px;background:var(--orange)}
.hero{position:absolute;left:0;top:180px;width:938px;height:366px;background:radial-gradient(circle at 40% 40%,var(--green-light),var(--green) 70%)}
.hero-visual{position:absolute;left:104px;top:76px;width:336px;height:248px;border-radius:6px;background:linear-gradient(160deg,#3a3a3a,#9aa0a0 70%,rgba(200,200,200,.3))}
.hero-kicker{position:absolute;left:546px;top:72px;font-weight:300;font-size:46px;line-height:1;color:var(--ink);letter-spacing:1px;white-space:nowrap}
.hero-title{position:absolute;left:546px;top:136px;font-family:"Bebas Neue",sans-serif;font-size:54px;line-height:1;color:var(--white)}
.hero-text{position:absolute;left:546px;top:200px;width:350px;font-size:11px;line-height:13px;color:var(--ink)}
.btn{position:absolute;left:547px;top:261px;width:91px;height:40px;background:var(--ink);color:var(--white);font-size:11px;font-weight:600;display:flex;align-items:center;justify-content:center;border-radius:2px}
.slider-dots{position:absolute;left:437px;top:337px;width:65px;height:14px;border-radius:7px;background:#5f8f24;display:flex;align-items:center;justify-content:center;gap:7px}
.slider-dots span{width:6px;height:6px;border-radius:50%;background:var(--white)}
.slider-dots span.is-current{background:transparent;border:1px solid var(--white)}
.welcome{position:absolute;left:0;top:578px;width:938px;text-align:center}
.welcome h1{font-family:"Bebas Neue",sans-serif;font-weight:400;font-size:31px;letter-spacing:1.5px;color:var(--ink);line-height:34px}
.welcome .tagline{margin-top:12px;font-style:italic;font-size:11.5px;color:var(--ink)}
.welcome .intro{margin:12px auto 0;width:858px;font-size:9.6px;line-height:16px;color:var(--text)}
.services-title{position:absolute;left:39px;top:749px;font-family:"Bebas Neue",sans-serif;font-weight:400;font-size:26px;letter-spacing:1.5px}
.service-card{position:absolute;top:808px;width:192px;height:245px;background:var(--orange);border-radius:3px;box-shadow:2px 3px 4px rgba(0,0,0,.25)}
.service-card .art{position:absolute;left:26px;top:16px;width:140px;height:176px;border-radius:4px}
.service-card .label{position:absolute;left:0;bottom:18px;width:100%;text-align:center;font-size:16px;font-weight:400;color:var(--ink)}
.site-footer{position:absolute;left:0;top:1085px;width:938px;height:115px;background:var(--footer)}
.footer-nav{position:absolute;left:40px;top:40px;font-size:10px;color:var(--white)}
.footer-nav span{margin:0 6px}
.copyright{position:absolute;left:40px;top:63px;font-size:9.5px;color:var(--white)}
.social{position:absolute;left:722px;top:43px;display:flex;gap:9px}
.social span{width:28px;height:28px;border-radius:50%;border:1.5px solid var(--white)}
</style>
</head>
<body>
<div class="top-bar"></div>
<header class="site-header">
  <div class="brand"><span class="brand-name">Lumen Consulting</span></div>
  <nav class="main-nav">
    <a href="#" class="is-active" style="left:40px">Home</a>
    <a href="#" style="left:133px">About Us</a>
    <a href="#" style="left:246px">Category</a>
    <a href="#" style="left:611px">Products</a>
    <a href="#" style="left:727px">Brands</a>
    <a href="#" style="left:830px">Contact Us</a>
  </nav>
  <div class="nav-marker"></div>
</header>
<section class="hero">
  <div class="hero-visual" role="img" aria-label="Smartphone and laptop computer photograph"></div>
  <div class="hero-kicker">MAJOR BRANDS</div>
  <div class="hero-title">ELECTRONICS</div>
  <p class="hero-text">Sed ut perspiciatis unde omnis iste natus error sit voluptatem accusantium doloremque laudantium, totam rem aperiam, eaque ipsa quae ab illo inventore veritatis</p>
  <div class="btn">READ MORE</div>
  <div class="slider-dots"><span class="is-current"></span><span></span><span></span><span></span></div>
</section>
<section class="welcome">
  <h1>WELCOME TO LUMEN</h1>
  <p class="tagline">NEW SUPPLY CHAIN CONSULTING BUSINESS</p>
  <p class="intro">Sed ut perspiciatis unde omnis iste natus error sit voluptatem accusantium doloremque laudantium, totam rem aperiam, eaque ipsa quae ab illo inventore veritatis et quasi architecto beatae vitae dicta sunt explicabo. Nemo enim ipsam voluptatem quia voluptas sit aspernatur aut odit aut fugit, sed quia consequuntur magni dolores eos qui ratione voluptatem sequi nesciunt. Neque porro quisquam est, qui dolorem ipsum quia dolor sit amet, consectetur, adipisci velit,</p>
</section>
<h2 class="services-title">SERVICES</h2>
<div class="service-card" style="left:40px"><div class="art" role="img" aria-label="Smartphone photograph" style="background:linear-gradient(#2a2a2a,#111)"></div><div class="label">ELECTRONICS</div></div>
<div class="service-card" style="left:264px"><div class="art" role="img" aria-label="Black and red jacket photograph" style="background:linear-gradient(160deg,#2b2b2b,#1a1a1a 60%,#b3262a)"></div><div class="label">APPAREL</div></div>
<div class="service-card" style="left:484px"><div class="art" role="img" aria-label="Toy panda bear illustration" style="background:linear-gradient(#c9d3e0,#3a3a3a)"></div><div class="label">TOY</div></div>
<div class="service-card" style="left:705px"><div class="art" role="img" aria-label="Diamond earrings and ring photograph" style="background:linear-gradient(#d8d8d8,var(--orange-dark))"></div><div class="label">JEWELLERY</div></div>
<footer class="site-footer">
  <div class="footer-nav">HOME<span>/</span>ABOUT US<span>/</span>CATEGORY<span>/</span>PRODUCTS<span>/</span>BRANDS<span>/</span>CONTACT US</div>
  <div class="copyright">© 2014 Lumen. All right reserved.</div>
  <div class="social" aria-label="Social links"><span></span><span></span><span></span><span></span><span></span></div>
</footer>
</body>
</html>
```